Bry Ta's Jar Lable for kids Christmas gifts

Looking to get a wrap around label made for a quart canning jar. I would like it to have my kids head on it also. I was thinking in a silhouette form on both ends of the wrap( added a quick sketch up). We will be canning Pickles and giving them away as gifts this year. Also might be selling a few at a frames market. The brand name is " Bry Ta's" ( at the moment) So if you could think of a cool logo around that would be awesome also. I am an Orange and Black fan but I am up for suggestions also. Do you think this might be something you could help me with?

The second attached graphic is what I would like my kids faces to look similer to. Art wise. The sketch is of what the ends of the labels need to look like. Not a full face but a half of each of there faces on both ends of the lable.

Colors
f78f20
000000
757575

Requirements
Nice to have
• antique lable feel

```html
<!DOCTYPE html>
<html lang="en">
<head>
<meta charset="utf-8">
<title>Bry Ta's Jar Label</title>
<link href="https://fonts.googleapis.com/css2?family=Arimo:wght@400&display=swap" rel="stylesheet">
<style>
  :root {
    --backdrop: #1c1c1c;
    --label-black: #141414;
    --paper-white: #ffffff;
    --portrait-tone: #3a3a3a;
    --accent-orange: #f78f20;
    --accent-grey: #757575;
  }
  html, body {
    margin: 0;
    padding: 0;
    width: 1200px;
    height: 960px;
    overflow: hidden;
    background: var(--backdrop);
    font-family: "Arimo", Arial, sans-serif;
  }
  .jar-label {
    position: absolute;
    left: 119px;
    top: 266px;
    width: 963px;
    height: 427px;
    background: var(--label-black);
    color: var(--paper-white);
    overflow: hidden;
  }
  .seam-band {
    position: absolute;
    left: 258px;
    top: 0;
    width: 116px;
    height: 100%;
    background: var(--paper-white);
  }
  .portrait-half {
    position: absolute;
    top: 94px;
    height: 238px;
    background: var(--portrait-tone);
  }
  .portrait-half--left {
    left: 181px;
    width: 77px;
    border-radius: 60px 0 0 70px;
  }
  .portrait-half--right {
    left: 374px;
    width: 73px;
    border-radius: 0 60px 70px 0;
  }
  .side-description {
    position: absolute;
    left: 522px;
    top: 44px;
    height: 340px;
    margin: 0;
    writing-mode: vertical-rl;
    transform: rotate(180deg);
    text-align: center;
    white-space: nowrap;
    font-size: 13.5px;
    line-height: 16px;
  }
  .brand-name {
    position: absolute;
    left: 694px;
    top: 50px;
    margin: 0;
    font-size: 56px;
    font-weight: 400;
    line-height: 1;
    white-space: nowrap;
    display: flex;
    align-items: center;
    gap: 10px;
  }
  .brand-dot {
    flex: none;
    width: 42px;
    height: 42px;
    border-radius: 50%;
    background: var(--accent-orange);
  }
  .front-description {
    position: absolute;
    left: 694px;
    top: 166px;
    margin: 0;
    white-space: nowrap;
    font-size: 13.5px;
    line-height: 14.8px;
  }
</style>
</head>
<body>
  <div class="jar-label">
    <div class="portrait-half portrait-half--left" role="img" aria-label="Line-art silhouette of the left half of a child's head with curly hair"></div>
    <div class="seam-band"></div>
    <div class="portrait-half portrait-half--right" role="img" aria-label="Line-art silhouette of the right half of a child's head with curly hair"></div>

    <p class="side-description">A pickled cucumber is a cucumber that has been<br>pickled in a brine, vinegar, or other solution and left to<br>ferment for a period of time, by either immersing the<br>cucumbers in an acidic solution or through souring by<br>lacto-fermentation</p>

    <h1 class="brand-name">Bry Ta's <span class="brand-dot"></span></h1>

    <p class="front-description">A pickled cucumber<br>is a cucumber that<br>has been pickled in a<br>brine, vinegar, or<br>other solution and left<br>to ferment for a<br>period of time, by<br>either immersing the<br>cucumbers in an<br>acidic solution or<br>through souring by<br>lacto-fermentation</p>
  </div>
</body>
</html>
```